EILT: Landing Page - EXPRESS VERSAND
Zielgruppe
Es soll in kurzer Zeit (max 48 Stunden) eine kleine Ladingpage entstehen. Expressversand / Import von China nach Deutschland . Aufgrund der stark steigenden Luftfrachtraten aus China heraus hat sich unsere Firma Fracht-Kapazitäten gesichert. Diese sollen nun angeboten werden. Über eine Ladingpage sollen Anfragen generiert werden. Diese Anfragen werden dann mit einem Angebot von uns beantwortet. Expressversand / Import von China nach Deutschland
Aufgabenstellung
Die Seite soll beinhalten:
- 1-2 Bilder (z. B. Luftfracht, Logistik, Flugzeug, Cargo, etc)
- kurzer erklärender Text: z.B. 'jetzt Angebot anfordern und günstig aus China per Express versenden.' Inkl. Abholung, Verzollung und Zustellung. Kurze Laufzeit von nur 3-5 Tagen. ab 45€ / Paket
- Anfrage Formular, bestehend aus: , Abholadresse in China/Post Code, ZielAdresse Deutschland, Sendungsinformationen (wie viele Kartons, wie schwer ist ein Karton und welche Abmessungen L/B/H ), wann ist die Sendung in China abholbereit, optional: Sendungsinhalt (Ware, Zolltarifnummer/HS Code) , Firma, Name, email adresse
- optional ein Header/Laufband etc mit: Bis zum 19. Nov 21 versenden - Ware bis GrauSonntag erhalten!
- 24h Servicehotline, Tel: 0987/213546
- 2-3 Kundenreferenzen: Bilder von Personen mit Text : „Schneller Versand - nur 4 Tage Laufzeit“ , „1A Service, ohne Probleme“ , „gute Preise - nur zu empfehlen.“
Unser Firmenlogo kann - muss aber nicht auftauchen.
In der farblichen Gestaltung haben Sie freie Hand und freuen uns auf Ihre Vorschläge.
Aufgrund der Dringlichkeit sollte diese Landingpage innerhalb 48 Stunden 'live ' gehen.
WICHTIG: Die Page sollte von Ihnen auch veröffentlich werden. Aktuell nutzen wir den Kelvo Homepagebaukasten. Die Page kann aber auch durch andere Anbieter veröffentlicht werden , zb Pagimundo

```html
<!DOCTYPE html>
<html lang="de">
<head>
<meta charset="utf-8">
<title>Expressversand China – Deutschland</title>
<link href="https://fonts.googleapis.com/css2?family=PT+Sans:wght@400;700&display=swap" rel="stylesheet">
<style>
:root{
  --purple:#7a2be0;
  --hero-a:#8a3fd9;
  --hero-b:#b866b8;
  --hero-c:#e3804a;
  --sky:#2aa9e2;
  --brick:#c94a36;
  --card-purple:#8b58e0;
  --card-red:#d46761;
  --star:#f7b733;
  --ink:#111;
  --footer:#e5e5e5;
  --white:#fff;
}
*{box-sizing:border-box;margin:0;padding:0}
html,body{width:1200px;height:816px;overflow:hidden;background:var(--white);font-family:"PT Sans",sans-serif}
.page{position:relative;width:1200px;height:816px}
.promo-bar{position:absolute;left:0;top:0;width:1200px;height:53px;display:flex;align-items:center;justify-content:center;color:var(--purple);font-weight:700;font-size:19.5px;box-shadow:0 2px 4px rgba(0,0,0,.15);z-index:2;background:var(--white)}
.hero{position:absolute;left:0;top:53px;width:1200px;height:477px;overflow:hidden}
.hero-visual{position:absolute;inset:0;background:linear-gradient(100deg,var(--hero-a) 0%,#9c4fcf 35%,var(--hero-b) 60%,var(--hero-c) 100%)}
.brand{position:absolute;left:153px;top:18px;display:flex;align-items:center;gap:8px;color:var(--white);font-weight:700;font-size:28px}
.brand-dot{width:30px;height:30px;border-radius:50%;background:var(--sky)}
.hero-title{position:absolute;left:150px;top:152px;color:var(--white);font-weight:700;font-size:44px;line-height:43px}
.hotline-label{position:absolute;left:185px;top:340px;color:var(--white);font-weight:700;font-size:25px}
.hotline{position:absolute;left:153px;top:377px;width:275px;height:46px;border-radius:23px;background:var(--brick);display:flex;align-items:center;gap:10px;padding-left:24px;color:var(--white);font-weight:700;font-size:30px}
.arrow{position:absolute;left:570px;top:98px;z-index:1}
.request{position:absolute;left:603px;top:44px;width:446px;height:390px;background:var(--sky)}
.request-intro{position:absolute;left:19px;top:13px;width:420px;color:var(--white);font-weight:700;font-size:15px;line-height:19.5px}
.field{position:absolute;width:201px;height:37px;background:var(--white);border-radius:2px;font-size:12.5px;color:var(--ink);padding-left:16px;display:flex;align-items:center;font-family:inherit}
.send{position:absolute;left:110px;top:331px;width:230px;height:41px;border-radius:22px;background:var(--brick);border:2px solid var(--white);color:var(--white);font-weight:700;font-size:17px;display:flex;align-items:center;justify-content:center;gap:12px}
.quote-mark{position:absolute;left:150px;top:543px}
.reviews-title{position:absolute;left:0;top:554px;width:1200px;text-align:center;font-weight:700;font-size:28px;color:var(--ink)}
.review{position:absolute;top:610px;width:289px;height:125px;color:var(--white);text-align:center}
.review-text{margin-top:15px;font-size:15.5px}
.reviewer{position:absolute;left:0;top:50px;width:100%;display:flex;justify-content:center;align-items:center;gap:10px}
.avatar{width:55px;height:55px;border-radius:50%;background:linear-gradient(135deg,#6b4a3a,#2c2624)}
.reviewer-info{text-align:left;font-size:12.5px}
.stars{display:flex;gap:1px;margin-top:3px}
.footer{position:absolute;left:0;top:771px;width:1200px;height:45px;background:var(--footer);display:flex;align-items:center;justify-content:center;font-size:12.5px;color:var(--ink)}
</style>
</head>
<body>
<div class="page">
  <div class="promo-bar">noch bis 19. November versenden und Sendung bis GrauSonntag herhalten!</div>

  <section class="hero">
    <div class="hero-visual" role="img" aria-label="Frachtflugzeug beim Start über einem Containerhafen mit Kränen, violett-orange getönt"></div>
    <div class="brand"><span class="brand-dot"></span>Frakto</div>
    <h1 class="hero-title">Expressversand /<br>Import von China<br>nach Deutschland</h1>
    <div class="hotline-label">24h Servicehotline</div>
    <div class="hotline">
      <svg width="26" height="26" viewBox="0 0 24 24" fill="none" stroke="#fff" stroke-width="1.8" stroke-linecap="round" stroke-linejoin="round"><path d="M5 3h3l2 5-2.5 1.5a11 11 0 0 0 7 7L16 14l5 2v3a2 2 0 0 1-2 2A16 16 0 0 1 3 5a2 2 0 0 1 2-2z"/><path d="M15 3a6 6 0 0 1 6 6M15 6.5a2.5 2.5 0 0 1 2.5 2.5"/></svg>
      0987/213546
    </div>

    <form class="request">
      <p class="request-intro">Jetzt Angebot anfordern und günstig aus China per Express versenden.' Inkl. Abholung, Verzollung und Zustellung. Kurze Laufzeit von nur 3-5 Tagen. ab 45€ / Paket</p>
      <div class="field" style="left:17px;top:91px">Firma</div>
      <div class="field" style="left:229px;top:91px">Name</div>
      <div class="field" style="left:18px;top:137px">Email Adresse</div>
      <div class="field" style="left:230px;top:137px">Abholadresse in China</div>
      <div class="field" style="left:19px;top:184px">Post Code</div>
      <div class="field" style="left:231px;top:184px">ZielAdresse Deutschland</div>
      <div class="field" style="left:20px;top:232px">Wie Viele Kartons</div>
      <div class="field" style="left:232px;top:232px">Karton Gewicht</div>
      <div class="field" style="left:21px;top:279px">Abmessungen &nbsp;L / W / H</div>
      <div class="send">
        <svg width="18" height="18" viewBox="0 0 24 24" fill="none" stroke="#fff" stroke-width="1.6" stroke-linejoin="round"><path d="M22 2L2 11l8 3 2 8z"/><path d="M22 2L10 14"/></svg>
        SENDEN
      </div>
    </form>
    <svg class="arrow" width="45" height="120" viewBox="0 0 45 120" fill="none" stroke="#fff" stroke-width="4" stroke-linecap="round"><path d="M40 4C15 18 0 55 30 108"/><path d="M14 103l17 6 3-18"/></svg>
  </section>

  <svg class="quote-mark" width="57" height="54" viewBox="0 0 57 54" fill="#e3e3e3"><path d="M2 54V28C2 12 10 3 24 0l2 6C17 9 14 15 14 22h10v32zM33 54V28C33 12 41 3 55 0l2 6c-9 3-12 9-12 16h10v32z"/></svg>
  <h2 class="reviews-title">Was under Kunde sagt</h2>

  <div class="review" style="left:153px;background:var(--card-purple)">
    <p class="review-text">Schneller Versand - nur 4 Tage Laufzeit</p>
    <div class="reviewer"><div class="avatar" role="img" aria-label="Porträtfoto des Kunden"></div>
      <div class="reviewer-info">Lorens Mai<div class="stars">
        <svg width="58" height="11" viewBox="0 0 58 11" fill="var(--star)"><path id="s" d="M5.5 0l1.6 3.6 3.9.3-3 2.6.9 3.9-3.4-2-3.4 2 .9-3.9-3-2.6 3.9-.3z"/><use href="#s" x="11.7"/><use href="#s" x="23.4"/><use href="#s" x="35.1"/><use href="#s" x="46.8"/></svg>
      </div></div>
    </div>
  </div>
  <div class="review" style="left:456px;background:var(--card-red)">
    <p class="review-text">1A Service, ohne Probleme</p>
    <div class="reviewer"><div class="avatar" role="img" aria-label="Porträtfoto des Kunden"></div>
      <div class="reviewer-info">Tarek Olm<div class="stars">
        <svg width="58" height="11" viewBox="0 0 58 11" fill="var(--star)"><use href="#s"/><use href="#s" x="11.7"/><use href="#s" x="23.4"/><use href="#s" x="35.1"/><use href="#s" x="46.8"/></svg>
      </div></div>
    </div>
  </div>
  <div class="review" style="left:759px;background:var(--sky)">
    <p class="review-text">Gute Preise - nur zu empfehlen.</p>
    <div class="reviewer"><div class="avatar" role="img" aria-label="Porträtfoto des Kunden"></div>
      <div class="reviewer-info">Lorens Mai<div class="stars">
        <svg width="58" height="11" viewBox="0 0 58 11" fill="var(--star)"><use href="#s"/><use href="#s" x="11.7"/><use href="#s" x="23.4"/><use href="#s" x="35.1"/><use href="#s" x="46.8"/></svg>
      </div></div>
    </div>
  </div>

  <footer class="footer">Copyright 2021. Alle Rechte vorbehalten.</footer>
</div>
</body>
</html>
```